A new presentation to our clients

we are a Real Estate agency, our website is www.dorelumia.com and it’s time to have a new, fashion and remarcable Business Card. we want to differentiate ourselves from other companies so we want a business card that differentiates us. we want the business card to impact our customers. in the competitive market that we have today, we have to be different and it is this difference that we seek

Target Market(s)

Real Estate Clients

Contact Information for Business Card

We search a totaly diferent card from the usual

Font styles to use
Sans Serif

Colors
e34197

Requirements
Must have
• Logo, adress, phone contact, e-mail, photo, and our website
Nice to have
• We would like to see a modern business card
Should not have
• Houses or building draws

```html
<!DOCTYPE html>
<html lang="en">
<head>
<meta charset="utf-8">
<title>Dore Lumia — Business Card</title>
<link href="https://fonts.googleapis.com/css2?family=Comfortaa:wght@700&family=Open+Sans:wght@400;600&display=swap" rel="stylesheet">
<style>
  :root {
    --brand-pink: #ea2a7b;
    --paper: #ffffff;
    --ink: #222222;
    --stage: #e9e9eb;
    --photo-dark: #2a2a2e;
    --photo-mid: #6b5a50;
  }
  * { box-sizing: border-box; margin: 0; padding: 0; }
  html, body { width: 1200px; height: 899px; overflow: hidden; }
  body {
    background: var(--stage);
    font-family: "Open Sans", sans-serif;
    position: relative;
  }
  .card {
    position: absolute;
    left: 290px;
    width: 620px;
    height: 354px;
    border-radius: 30px;
    overflow: hidden;
    box-shadow: 0 6px 18px rgba(0,0,0,0.18);
  }
  .card-back { top: 50px; background: var(--brand-pink); }
  .card-front { top: 470px; background: var(--paper); }

  .notch {
    position: absolute;
    width: 56px; height: 56px;
    border-radius: 50%;
    background: var(--paper);
  }
  .notch-right { right: -28px; top: 52px; }
  .notch-left { left: -28px; bottom: 52px; }

  .wordmark {
    font-family: "Comfortaa", sans-serif;
    font-weight: 700;
    letter-spacing: 1px;
    white-space: nowrap;
  }
  .card-back .wordmark {
    position: absolute;
    left: 0; right: 0; top: 142px;
    text-align: center;
    font-size: 66px;
    color: var(--paper);
  }
  .card-front .wordmark {
    position: absolute;
    left: 50px; top: 70px;
    font-size: 46px;
    color: var(--brand-pink);
  }

  .address, .contact-list {
    position: absolute;
    left: 56px;
    color: var(--ink);
    font-size: 14px;
    line-height: 20px;
  }
  .address { top: 158px; }
  .contact-list { top: 204px; list-style: none; }
  .contact-list li { display: flex; align-items: center; gap: 8px; }
  .contact-list svg { width: 12px; height: 12px; fill: var(--brand-pink); flex: none; }

  .photo {
    position: absolute;
    right: 0; top: 0; bottom: 0;
    width: 250px;
    background: linear-gradient(160deg, var(--photo-mid) 0%, var(--photo-dark) 55%, #161618 100%);
    clip-path: polygon(28% 0, 100% 0, 100% 100%, 0 100%, 8% 40%);
  }

  .name-band {
    position: absolute;
    left: 0; bottom: 0;
    width: 410px; height: 78px;
    background: var(--brand-pink);
    clip-path: polygon(0 0, 100% 0, 92% 100%, 0 100%);
    color: var(--paper);
    padding: 12px 0 0 56px;
  }
  .person-name {
    font-family: "Comfortaa", sans-serif;
    font-weight: 700;
    font-size: 30px;
    line-height: 34px;
  }
  .person-role { font-size: 14px; line-height: 18px; padding-left: 22px; }
</style>
</head>
<body>
  <section class="card card-back">
    <span class="notch notch-right"></span>
    <span class="notch notch-left"></span>
    <div class="wordmark">Dore Lumia</div>
  </section>

  <section class="card card-front">
    <div class="wordmark">Dore Lumia</div>
    <p class="address">48 Harbour Lane, Suite B<br>London, UK B0034C</p>
    <ul class="contact-list">
      <li><svg viewBox="0 0 12 12"><path d="M3 1 L5 3 L4 4.5 C5 6.5 5.5 7 7.5 8 L9 7 L11 9 L9.5 11 C5 10.5 1.5 7 1 2.5 Z"/></svg>020 481 3925</li>
      <li><svg viewBox="0 0 12 12"><path d="M1 3 H11 V10 H1 Z M1 3 L6 7 L11 3" stroke="#fff" stroke-width="0.8"/></svg>info@dorelumia.com</li>
      <li><svg viewBox="0 0 12 12"><circle cx="6" cy="6" r="5"/><path d="M1 6 H11 M6 1 V11 M2 3.5 H10 M2 8.5 H10" stroke="#fff" stroke-width="0.7" fill="none"/></svg>www.dorelumia.com</li>
    </ul>
    <div class="photo" role="img" aria-label="Portrait photo of the director in a dark blazer"></div>
    <div class="name-band">
      <div class="person-name">Mark Ellison</div>
      <div class="person-role">Director</div>
    </div>
  </section>
</body>
</html>
```